Company Profile for Academic and Study Abroad Services

I am looking for Power Point Design for company Profile . the company is academic and study abroad services. you can visit the website which is www.korvelan.ae . the colour i prefer is Dark Blue + White + Black . you can find all the content for power point and logo and some picture i need you to add it.

Target Market(s)

Students who wants to study abroad. Universities . Learning centre.

Industry/Entity Type

Education

Font styles to use
Serif
Sans Serif

Colors
0555a3
ffffff
000000
aaaaaa

Requirements
Must have
• Must Have Images for each slides.
Nice to have
• infographic. Images related to the study abroad

```html
<!DOCTYPE html>
<html lang="en">
<head>
<meta charset="utf-8">
<title>Korvelan – Quote Slides</title>
<link rel="stylesheet" href="https://fonts.googleapis.com/css2?family=Montserrat:wght@700;800&family=Questrial&display=swap">
<style>
  :root {
    --page-bg: #e6e6f3;
    --slide-bg: #ffffff;
    --ink: #000000;
    --text: #2b2b2b;
    --muted: #aaaaaa;
    --line-grey: #a9a9a9;
    --brand: #0b2a4a;
    --photo-dark: #3a3a3a;
    --photo-light: #9a9a9a;
    --photo-warm: #c9a88a;
    --photo-cloth: #f1f1ef;
  }
  * { box-sizing: border-box; margin: 0; padding: 0; }
  html, body { width: 708px; height: 1200px; overflow: hidden; }
  body { background: var(--page-bg); font-family: "Questrial", sans-serif; color: var(--text); position: relative; }

  .slide {
    position: absolute; left: 6px; width: 696px; height: 390px;
    background: var(--slide-bg); overflow: hidden;
  }
  .slide--one { top: 6px; }
  .slide--two { top: 405px; }
  .slide--three { top: 803px; }

  .rule { position: absolute; background: var(--ink); }
  .slide--one .rule { background: var(--line-grey); width: 3px; }
  .rule--v { width: 3px; }
  .rule--h { height: 3px; }

  .portrait {
    position: absolute; border-radius: 50%;
    border: 3px solid var(--ink); overflow: hidden;
  }
  .slide--one .portrait { border: 4px solid var(--line-grey); }
  .portrait__fill { width: 100%; height: 100%; border-radius: 50%; border: 4px solid var(--slide-bg); }
  .portrait--mono .portrait__fill { background: radial-gradient(circle at 50% 40%, var(--photo-light), var(--photo-dark) 75%); }
  .portrait--colour .portrait__fill { background: radial-gradient(circle at 50% 45%, var(--photo-warm) 0 35%, var(--photo-cloth) 60%, #d9d6cf); }

  .quote {
    position: absolute; transform: translateX(-50%);
    text-align: center; white-space: nowrap;
  }
  .quote__mark {
    font-family: "Montserrat", sans-serif; font-weight: 800;
    font-size: 34px; line-height: 24px; height: 22px; color: var(--ink); overflow: hidden;
  }
  .slide--one .quote__mark { color: var(--muted); }
  .quote__text { font-size: 13.5px; line-height: 18px; margin: 10px 0 6px; color: var(--text); }
  .quote__author {
    font-family: "Montserrat", sans-serif; font-weight: 700;
    font-size: 11px; color: var(--muted); margin-top: 8px;
  }

  .brand {
    position: absolute; right: 18px; bottom: 18px;
    font-family: "Montserrat", sans-serif; font-weight: 800;
    font-size: 12px; color: var(--brand); letter-spacing: 0.5px;
  }
</style>
</head>
<body>

<section class="slide slide--one">
  <div class="rule rule--v" style="left:126px;top:0;height:212px"></div>
  <div class="rule rule--v" style="left:568px;top:166px;height:224px"></div>
  <div class="portrait portrait--mono" style="left:501px;top:31px;width:136px;height:136px">
    <div class="portrait__fill" role="img" aria-label="Black and white portrait of Elias Montoro"></div>
  </div>
  <div class="portrait portrait--colour" style="left:56px;top:210px;width:142px;height:142px">
    <div class="portrait__fill" role="img" aria-label="Portrait of H.E. Rashid Bin Saeed Al Qadeer"></div>
  </div>
  <div class="quote" style="left:349px;top:46px">
    <div class="quote__mark">“</div>
    <p class="quote__text">Education is the most powerful<br>weapon which you can use to<br>change the world</p>
    <div class="quote__mark">”</div>
    <p class="quote__author">Elias Montoro</p>
  </div>
  <div class="quote" style="left:365px;top:210px">
    <div class="quote__mark">“</div>
    <p class="quote__text">There is no place in the future for<br>those who lack science and<br>knowledge</p>
    <div class="quote__mark">”</div>
    <p class="quote__author">H.E. Rashid Bin Saeed Al Qadeer</p>
  </div>
  <div class="brand">KORVELAN</div>
</section>

<section class="slide slide--two">
  <div class="rule rule--v" style="left:126px;top:0;height:212px"></div>
  <div class="rule rule--v" style="left:568px;top:166px;height:224px"></div>
  <div class="portrait portrait--mono" style="left:501px;top:31px;width:136px;height:136px">
    <div class="portrait__fill" role="img" aria-label="Black and white portrait of Elias Montoro"></div>
  </div>
  <div class="portrait portrait--colour" style="left:56px;top:210px;width:142px;height:142px">
    <div class="portrait__fill" role="img" aria-label="Portrait of H.E. Rashid Bin Saeed Al Qadeer"></div>
  </div>
  <div class="quote" style="left:349px;top:46px">
    <div class="quote__mark">“</div>
    <p class="quote__text">Education is the most powerful<br>weapon which you can use to<br>change the world</p>
    <div class="quote__mark">”</div>
    <p class="quote__author">Elias Montoro</p>
  </div>
  <div class="quote" style="left:365px;top:210px">
    <div class="quote__mark">“</div>
    <p class="quote__text">There is no place in the future for<br>those who lack science and<br>knowledge</p>
    <div class="quote__mark">”</div>
    <p class="quote__author">H.E. Rashid Bin Saeed Al Qadeer</p>
  </div>
  <div class="brand">KORVELAN</div>
</section>

<section class="slide slide--three">
  <div class="rule rule--h" style="left:0;top:141px;width:210px"></div>
  <div class="rule rule--h" style="left:516px;top:292px;width:180px"></div>
  <div class="portrait portrait--colour" style="left:208px;top:69px;width:148px;height:148px">
    <div class="portrait__fill" role="img" aria-label="Portrait of H.E. Rashid Bin Saeed Al Qadeer"></div>
  </div>
  <div class="portrait portrait--mono" style="left:340px;top:223px;width:142px;height:142px">
    <div class="portrait__fill" role="img" aria-label="Black and white portrait of Elias Montoro"></div>
  </div>
  <div class="quote" style="left:529px;top:90px">
    <div class="quote__mark">“</div>
    <p class="quote__text">There is no place in the future for<br>those who lack science and<br>knowledge</p>
    <div class="quote__mark">”</div>
    <p class="quote__author">H.E. Rashid Bin Saeed Al Qadeer</p>
  </div>
  <div class="quote" style="left:150px;top:240px">
    <div class="quote__mark">“</div>
    <p class="quote__text">Education is the most powerful<br>weapon which you can use to<br>change the world</p>
    <div class="quote__mark">”</div>
    <p class="quote__author">Elias Montoro</p>
  </div>
  <div class="brand">KORVELAN</div>
</section>

</body>
</html>
```